NZ First of it's kind solutions directory and marketplace for busy Mums needs a business card design

We need a business card design for our new nationwide business in NZ (long term plans to go global). We provide solutions to the everyday challenges that busy Mums face by connecting them with quality communities and suppliers of carefully selected, relevant products and services. We sell direct via our online marketplace. The final design should communicate our values of inclusivity, quality and smart solutions. Colours should incorporate our logo colour palette of #477077 and #6ba8b2. Our website is at https://www.brightnestly.com

Target Market(s)

busy Mums, Age 28 – 50, female, income over $100K, location main centres NZ primarily but NZ wide. Is likely juggling work or career with a young family. Probably had hobbies which have fallen by the wayside.
-Wants to succeed in her chosen career without compromising on family life
-to successfully juggle her career without feeling like she is compromising her children
- Is time poor, something always has to give and it’s generally her health (she’ll stay up late, get stressed)
- probably ex corporate or professional career. Has discretional income

Industry/Entity Type

Business

Contact Information for Business Card

Jodie Farnsworth, Founder, BrightNestly.com (Strapline Browse; Pick; Sorted), 48 Kowhai Terrace, Hillsborough, Auckland 1058, New Zealand. Mob: 021 437 518 Ph: +64 (0)9 584 7163

Font styles to use
Other font styles liked:
• Raleway, and/or Architects Daughter

Colors
00a990
33b8a4
86cfc6
cfeae6

Requirements
Must have
• the above details, streamline. the logo and colours associated with those logos
Should not have
• foil or metallic colours

```html
<!DOCTYPE html>
<html lang="en">
<head>
<meta charset="utf-8">
<title>BrightNestly business card</title>
<link rel="stylesheet" href="https://fonts.googleapis.com/css2?family=Raleway:wght@400;500;700&display=swap">
<style>
  :root {
    --teal: #00ab8f;
    --teal-line: #33b8a4;
    --brand-dark: #477077;
    --brand-light: #6ba8b2;
    --pale: #cfeae6;
    --white: #ffffff;
    --backdrop: #e6e7e8;
  }
  * { margin: 0; padding: 0; box-sizing: border-box; }
  html, body { width: 1200px; height: 1000px; overflow: hidden; }
  body {
    position: relative;
    background: var(--backdrop);
    font-family: "Raleway", Arial, sans-serif;
  }
  .card {
    position: absolute;
    border-radius: 36px;
    overflow: hidden;
  }
  /* Front */
  .card-front {
    left: 150px; top: 102px; width: 628px; height: 358px;
    background: var(--white);
  }
  .card-front .frame {
    position: absolute;
    left: 27px; top: 27px; width: 575px; height: 303px;
    border: 1.5px solid var(--teal-line);
    border-radius: 28px;
  }
  .front-brand {
    position: absolute;
    left: 104px; top: 148px;
    display: flex; align-items: center; gap: 18px;
  }
  .front-brand .mark {
    width: 52px; height: 52px; border-radius: 50%;
    background: var(--brand-dark);
  }
  .front-brand .name {
    font-weight: 700; font-size: 52px; letter-spacing: -1px;
    color: var(--brand-dark);
  }
  /* Back */
  .card-back {
    left: 370px; top: 546px; width: 637px; height: 362px;
    background: var(--teal);
    color: var(--white);
  }
  .holder-name {
    position: absolute; left: 46px; top: 72px;
    font-size: 27px; font-weight: 400;
  }
  .holder-role {
    position: absolute; left: 46px; top: 114px;
    font-size: 18px; font-weight: 500;
  }
  .back-brand {
    position: absolute; left: 360px; top: 80px;
    display: flex; align-items: center; gap: 10px;
  }
  .back-brand .mark {
    width: 28px; height: 28px; border-radius: 50%;
    background: var(--pale);
  }
  .back-brand .name {
    font-weight: 700; font-size: 28px; letter-spacing: -0.5px;
    color: var(--white);
  }
  .divider {
    position: absolute; left: 0; top: 173px; width: 100%; height: 2px;
    background: var(--white);
  }
  .address-band {
    position: absolute; left: 108px; top: 176px; width: 540px; height: 26px;
    background: var(--white);
    border-radius: 0 0 0 14px;
    clip-path: polygon(0 0, 100% 0, 100% 100%, 14px 100%);
  }
  .address {
    position: absolute; left: 134px; top: 180px;
    font-size: 17px; font-weight: 500; color: var(--teal);
    white-space: nowrap;
  }
  .contacts {
    position: absolute; left: 46px; top: 226px;
    list-style: none;
  }
  .contacts li {
    display: flex; align-items: center; height: 34px;
    font-size: 19px; font-weight: 500; white-space: nowrap;
  }
  .contacts svg { width: 22px; height: 22px; margin-right: 16px; flex: none; }
  .contacts .landline span { margin-left: 6px; }
  .strapline { font-size: 14px; margin-left: 6px; }
</style>
</head>
<body>

<section class="card card-front">
  <div class="frame"></div>
  <div class="front-brand">
    <div class="mark"></div>
    <div class="name">BrightNestly</div>
  </div>
</section>

<section class="card card-back">
  <div class="holder-name">Jodie Farnsworth</div>
  <div class="holder-role">Founder</div>
  <div class="back-brand">
    <div class="mark"></div>
    <div class="name">BrightNestly</div>
  </div>
  <div class="divider"></div>
  <div class="address-band"></div>
  <div class="address">48 Kowhai Terrace, Hillsborough, Auckland 1058, New Zealand</div>
  <ul class="contacts">
    <li class="landline">
      <svg viewBox="0 0 24 24" aria-hidden="true"><path fill="#fff" d="M3 7c0-2 4-4 9-4s9 2 9 4v2h-5V7.5c-1.3-.5-2.6-.7-4-.7s-2.7.2-4 .7V9H3z"/><path fill="#fff" d="M7 10h10l3 10H4z"/><circle cx="12" cy="15" r="2.6" fill="#00ab8f"/></svg>
      <span>+64 (0)9 584 7163</span>
    </li>
    <li>
      <svg viewBox="0 0 24 24" aria-hidden="true"><path fill="#fff" d="M6.6 10.8a15 15 0 0 0 6.6 6.6l2.2-2.2c.3-.3.7-.4 1-.2 1.1.4 2.3.6 3.6.6.6 0 1 .4 1 1V20c0 .6-.4 1-1 1A17 17 0 0 1 3 4c0-.6.4-1 1-1h3.5c.6 0 1 .4 1 1 0 1.3.2 2.5.6 3.6.1.3 0 .7-.2 1z"/></svg>
      <span>021 437 518</span>
    </li>
    <li>
      <svg viewBox="0 0 24 24" aria-hidden="true"><g fill="none" stroke="#fff" stroke-width="1.8"><circle cx="12" cy="12" r="9.5"/><ellipse cx="12" cy="12" rx="4" ry="9.5"/><path d="M2.5 12h19M4 7h16M4 17h16"/></g></svg>
      <span>www.brightnestly.com</span><span class="strapline">( Strapline Browse; Pick; Sorted )</span>
    </li>
  </ul>
</section>

</body>
</html>
```